Billboard for Post Frame Construction Company

We need a billboard designed for a post frame construction company.
The billboard needs to have:
enclosed red barn as base picture
Cedarline Frame Works logo
Phone number (406) 555-0148
cedarlineframe.example
FREE QUOTE
Garages, Hobby Shops, Equestrian, Barndominiums, Commercial and more...
This billboard is scheduled to be in a rural part of Montana outside of Stevensvile, MT. The text must be legible on a highway.
Updates
Please do not add extra text that will make the billboard crowded or busy. The billboard is for a busy rural highway and the text needs to be visible. Thank you!
Requirements
Must have
- FREE QUOTE
Updated summer photo attached.
Nice to have
- Please use the updated summer photo for the billboard.
Please make sure the logo is prominent.
Should not have
- Extras that make the billboard too busy.
Do not add phone or web icons. Do not add the client tag line or anything extra. The client wants a simple billboard that is not busy and distracting.

```html
<!DOCTYPE html>
<html lang="en">
<head>
<meta charset="utf-8">
<title>Cedarline Frame Works – Billboard</title>
<link rel="stylesheet" href="https://fonts.googleapis.com/css2?family=Montserrat:wght@400;600;700;800&display=swap">
<style>
  :root {
    --navy: #243f91;
    --ink: #1b1b1b;
    --slate: #545454;
    --rule: #b9b9b9;
    --paper: #ffffff;
    --backdrop: #e6e6e6;
    --logo-ink: #2f3440;
  }
  * { margin: 0; padding: 0; box-sizing: border-box; }
  html, body {
    width: 1067px;
    height: 1200px;
    overflow: hidden;
    background: var(--backdrop);
  }
  .billboard {
    position: absolute;
    left: 33px;
    top: 425px;
    width: 1000px;
    height: 350px;
    background: var(--paper);
    box-shadow: 0 6px 18px rgba(0,0,0,0.18);
    font-family: "Montserrat", sans-serif;
    color: var(--ink);
    overflow: hidden;
  }
  .billboard-shapes {
    position: absolute;
    inset: 0;
  }
  .free-quote {
    position: absolute;
    left: 24px;
    top: 42px;
    width: 450px;
    height: 104px;
    background: var(--slate);
    color: var(--paper);
    font-weight: 800;
    font-size: 56px;
    line-height: 104px;
    text-align: center;
    letter-spacing: 1px;
  }
  .services {
    position: absolute;
    left: 24px;
    top: 198px;
    display: grid;
    grid-template-columns: 150px 180px 120px;
    row-gap: 16px;
    list-style: none;
    font-weight: 600;
    font-size: 17px;
    line-height: 20px;
  }
  .service {
    display: flex;
    align-items: center;
    gap: 7px;
    white-space: nowrap;
  }
  .service svg { width: 16px; height: 16px; flex: none; }
  .service.more { font-weight: 400; padding-left: 23px; }
  .brand-name {
    position: absolute;
    right: 30px;
    top: 34px;
    text-align: right;
    font-weight: 800;
    font-size: 36px;
    line-height: 1.1;
    letter-spacing: 1.5px;
    color: var(--logo-ink);
  }
  .phone {
    position: absolute;
    left: 30px;
    top: 289px;
    height: 61px;
    display: flex;
    align-items: center;
    color: var(--paper);
    font-weight: 700;
    font-size: 40px;
    letter-spacing: 3px;
  }
  .website {
    position: absolute;
    left: 512px;
    top: 289px;
    width: 488px;
    height: 51px;
    display: flex;
    align-items: center;
    justify-content: center;
    color: var(--paper);
    font-weight: 700;
    font-size: 25px;
    letter-spacing: 1px;
    white-space: nowrap;
  }
</style>
</head>
<body>
  <section class="billboard">
    <svg class="billboard-shapes" viewBox="0 0 1000 350" width="1000" height="350">
      <defs>
        <linearGradient id="barnScene" x1="0" y1="0" x2="0" y2="1">
          <stop offset="0" stop-color="#eef3f8"/>
          <stop offset="0.38" stop-color="#c9d6e4"/>
          <stop offset="0.55" stop-color="#c2545a"/>
          <stop offset="0.82" stop-color="#b8424a"/>
          <stop offset="1" stop-color="#a3a36a"/>
        </linearGradient>
      </defs>
      <polygon class="barn-photo" role="img" aria-label="Photo of an enclosed red post-frame barn in a summer pasture with mountains behind"
               points="566,0 1000,0 1000,289 472,289" fill="url(#barnScene)"/>
      <line x1="566" y1="0" x2="472" y2="289" stroke="var(--navy)" stroke-width="2"/>
      <polygon points="509,178 472,289 458,289 505,178" fill="var(--navy)"/>
      <line x1="24" y1="174" x2="487" y2="174" stroke="var(--rule)" stroke-width="1"/>
      <rect x="52" y="172" width="66" height="4" rx="2" fill="var(--navy)"/>
      <polygon points="0,289 452,289 484,350 0,350" fill="var(--navy)"/>
      <polygon points="466,289 1000,289 1000,340 493,340" fill="var(--slate)"/>
      <rect x="488" y="340" width="512" height="10" fill="var(--navy)"/>
    </svg>

    <div class="free-quote">FREE QUOTE</div>

    <ul class="services">
      <li class="service"><svg viewBox="0 0 16 16"><path d="M1 7 8 2l7 5v8H1z M4 15V9h8v6" fill="none" stroke="var(--navy)" stroke-width="1.4"/></svg>Garages</li>
      <li class="service"><svg viewBox="0 0 16 16"><path d="M4 15 6 8 3 5l4-3 5 3v10" fill="none" stroke="var(--navy)" stroke-width="1.4"/></svg>Equestrian</li>
      <li class="service"><svg viewBox="0 0 16 16"><path d="M2 15V6h12v9z M1 6l7-4 7 4 M5 9h2v2H5z M9 9h2v2H9z" fill="none" stroke="var(--navy)" stroke-width="1.4"/></svg>Commercial</li>
      <li class="service"><svg viewBox="0 0 16 16"><path d="M2 2h12v13H2z M5 6h6 M5 9h6 M5 12h6" fill="none" stroke="var(--navy)" stroke-width="1.4"/></svg>Hobby Shops</li>
      <li class="service"><svg viewBox="0 0 16 16"><path d="M2 15V7l6-5 6 5v8z M6 15v-4h4v4" fill="none" stroke="var(--navy)" stroke-width="1.4"/></svg>Barndominiums</li>
      <li class="service more">and more...</li>
    </ul>

    <div class="brand-name">CEDARLINE<br>FRAME WORKS</div>

    <div class="phone">(406) 555-0148</div>

    <div class="website">www.cedarlineframe.example</div>
  </section>
</body>
</html>
```